Yoga Studio - Class Timetable Flyer

We require a double sided, size DL (1/3 A4) flyer with our class timetable included.
We would like the final flyer to have.
Side A : Yoga image, logo, address, website, contact phone number, and in big font $40 Introductory Month.
Side B: Clear easy to read timetable, class descriptions and website.
Thank you.
Yours kindly,
Nadia
87d0c7
86cae7
85acd3

```html
<!DOCTYPE html>
<html lang="en">
<head>
<meta charset="utf-8">
<title>Stillwater Studio – Class Timetable Flyer</title>
<link href="https://fonts.googleapis.com/css2?family=Arimo:wght@400;700&family=PT+Sans&display=swap" rel="stylesheet">
<style>
:root{
  --teal:#6ddcd0;
  --teal-text:#5fcfc4;
  --ink:#1e1e1e;
  --black:#000;
  --white:#fff;
  --rule:#d6d6d6;
  --stage:#6b4a30;
}
*{margin:0;padding:0;box-sizing:border-box}
html,body{width:1143px;height:1200px;overflow:hidden}
body{background:var(--stage);font-family:"Arimo",Arial,sans-serif;position:relative}
.flyer{position:absolute;width:489px;height:1037px;overflow:hidden}
.flyer--front{left:64px;top:44px;background:var(--black);color:var(--white)}
.flyer--back{left:588px;top:36px;background:var(--white);color:var(--ink)}
.brand{position:absolute;text-align:center;color:var(--teal-text);font-weight:400}
.brand__mark{display:block;margin:0 auto 8px;width:64px;height:64px;border-radius:50%;background:var(--teal-text)}
.brand__name{font-size:38px;line-height:1;letter-spacing:1px}
.brand__tag{font-size:9px;letter-spacing:2px;margin-top:6px;white-space:nowrap}
.flyer--front .brand{left:0;width:220px;top:60px}
.flyer--back .brand{left:0;width:489px;top:20px}
.photo{position:absolute;border-radius:50%}
.photo--arm{left:209px;top:64px;width:274px;height:274px;background:radial-gradient(circle at 45% 50%,#d8d8d8,#9a9a9a 70%,#6a6a6a)}
.photo--bow{left:12px;top:250px;width:274px;height:274px;background:radial-gradient(circle at 55% 45%,#e6e6e6,#b8b8b8 65%,#7c7c7c)}
.ghost{position:absolute;left:310px;top:390px;width:130px;height:130px;border-radius:50%;background:#1c1c1c}
.promo{position:absolute;left:0;width:489px;text-align:center;font-weight:400}
.promo__title{top:570px;font-size:32px}
.promo__price{color:var(--teal)}
.promo__lead{top:616px;font-size:18px;line-height:27px}
.promo__note{top:710px;font-size:21px;line-height:34px}
.contact{position:absolute;left:0;width:489px;top:864px;list-style:none;text-align:center;font-size:19px}
.contact li{height:38px;display:flex;align-items:center;justify-content:center;gap:10px}
.contact svg{width:18px;height:18px;fill:var(--white)}
.cta{position:absolute;left:0;bottom:0;width:489px;height:54px;background:var(--teal);color:var(--black);display:flex;align-items:center;padding-left:60px;gap:20px}
.flyer--back .cta{height:52px}
.cta__label{font-size:33px}
.cta__phone{font-size:20px;display:flex;align-items:center;gap:6px}
.cta__phone svg{width:20px;height:20px}
.timetable__title{position:absolute;top:196px;left:0;width:489px;text-align:center;font-family:"PT Sans",Arial,sans-serif;font-size:24px;font-weight:400;color:var(--black)}
.row{position:absolute;left:18px;display:grid;grid-template-columns:86px 88px 143px 129px;column-gap:3px;height:24px;font-size:16px}
.row span{display:flex;align-items:center;justify-content:center;border-bottom:2px solid var(--rule);border-right:2px solid var(--rule);background:var(--white)}
.row span:first-child{color:var(--teal-text)}
.row--head span{background:var(--teal);color:var(--white)!important;border:none}
.desc{position:absolute;left:17px;top:576px;width:455px;font-size:15.5px;line-height:20px;text-align:justify;color:#333}
.desc p{margin-bottom:18px}
.desc b{font-size:18px;color:var(--ink)}
.web{position:absolute;left:0;width:489px;top:948px;text-align:center;font-size:16px;color:var(--ink);display:flex;align-items:center;justify-content:center;gap:8px}
.web svg{width:16px;height:16px}
</style>
</head>
<body>
<section class="flyer flyer--front">
  <div class="brand"><span class="brand__mark"></span><div class="brand__name">stillwater</div><div class="brand__tag">YOGA · FITNESS · AQUA</div></div>
  <div class="photo photo--arm" role="img" aria-label="Photo of a woman holding an arm-balance yoga pose"></div>
  <div class="photo photo--bow" role="img" aria-label="Photo of a woman in a bow yoga pose"></div>
  <div class="ghost"></div>
  <h1 class="promo promo__title"><span class="promo__price">$40</span> Introductory Month</h1>
  <p class="promo promo__lead">Come &amp; Join Stillwater Yoga, Fitness Today &amp; Avail<br>Great Discount for the first time members</p>
  <p class="promo promo__note">Please present concession card and ID<br>for concession prices<br>Available to full-time students only</p>
  <ul class="contact">
    <li><svg viewBox="0 0 24 24"><path d="M12 2a7 7 0 0 0-7 7c0 5 7 13 7 13s7-8 7-13a7 7 0 0 0-7-7zm0 9.5A2.5 2.5 0 1 1 12 6a2.5 2.5 0 0 1 0 5.5z"/></svg>42 Wattle Grove, Kinglake Vic 3763</li>
    <li><svg viewBox="0 0 24 24"><path d="M2 5h20v14H2zM3 6l9 7 9-7" stroke="#000" stroke-width="1.5"/></svg>nadiamarlow@cloud.com</li>
    <li><svg viewBox="0 0 24 24" fill="none" stroke="#fff" stroke-width="1.5" style="fill:none"><circle cx="12" cy="12" r="9"/><path d="M3 12h18M12 3c3 3 3 15 0 18M12 3c-3 3-3 15 0 18"/></svg>www.stillwaterstudio.com.au</li>
  </ul>
  <div class="cta"><span class="cta__label">Get In Today</span><span class="cta__phone"><svg viewBox="0 0 24 24" fill="none" stroke="#000" stroke-width="1.6"><circle cx="12" cy="12" r="10"/><path d="M9 7l2 3-1.5 1.5a7 7 0 0 0 3 3L14 13l3 2-1.5 2.5C11 17 7 13 6.5 8.5z" fill="#000"/></svg>0412-555-019</span></div>
</section>

<section class="flyer flyer--back">
  <div class="brand"><span class="brand__mark" style="width:70px;height:70px"></span><div class="brand__name">stillwater</div><div class="brand__tag">STUDIO · YOGA · FITNESS · AQUA</div></div>
  <h2 class="timetable__title">Our Class Time Table</h2>
  <div class="row row--head" style="top:227px"><span>Time</span><span>Day</span><span>Activity</span><span>Workout Time</span></div>
  <div class="row" style="top:252px"><span>9.30am</span><span>Tues</span><span>Hot</span><span>90 mins</span></div>
  <div class="row" style="top:277px"><span></span><span>Thurs</span><span>Power Vinyasa</span><span>75 mins</span></div>
  <div class="row" style="top:302px"><span></span><span>Sat</span><span>Power Vinyasa</span><span>90 mins</span></div>
  <div class="row" style="top:332px"><span>11:00am</span><span>Thurs</span><span>Power Essential</span><span>60mins</span></div>
  <div class="row" style="top:362px"><span>01:00pm</span><span>Wed</span><span>Hot</span><span>90 mins</span></div>
  <div class="row" style="top:392px"><span>04:30pm</span><span>Sun</span><span>Power Vinyasa</span><span>40 mins</span></div>
  <div class="row" style="top:422px"><span>06:30pm</span><span>Mon</span><span>Power Vinyasa</span><span>60 mins</span></div>
  <div class="row" style="top:447px"><span></span><span>Tues</span><span>Hot</span><span>90 mins</span></div>
  <div class="row" style="top:472px"><span></span><span>Fri</span><span>Funky Flow</span><span>75 mins</span></div>
  <div class="row" style="top:497px"><span></span><span>Sun</span><span>Yin</span><span>60 mins</span></div>
  <div class="row" style="top:527px"><span>06:30pm</span><span>Mon</span><span>Power Essential</span><span>60 mins</span></div>
  <div class="desc">
    <p><b>Funky Flow</b> - Finish off the week and head into the weekend with a joyful flowing class to a playlist of funky beats. Charity class by donation, suggested $10. Please place cash only in the charity donation box. Frequent guest teachers.</p>
    <p><b>Hot</b> - Dynamic sequence of Strength and Breathing exercises. Suitable for beginners. Heat 37 = degrees.</p>
    <p><b>Power Essentials</b> - Flowing Practice with space and time to Align and understand the poses deeply, building muscular strength and endurance. Ideal for beginners.</p>
    <p><b>Power Vinyasa</b> - Strong, Dynamic, Flowing practice ideal for building physical power, flexibility and mental resilience. Heat = 30 degrees</p>
    <p><b>Yin</b> - Long, Slow, Deep practice with a focus on supporting the body to release our deep internal structures of connective tissue.</p>
  </div>
  <p class="web"><svg viewBox="0 0 24 24" fill="none" stroke="#1e1e1e" stroke-width="1.5"><circle cx="12" cy="12" r="9"/><path d="M3 12h18M12 3c3 3 3 15 0 18M12 3c-3 3-3 15 0 18"/></svg>www.stillwaterstudio.com.au</p>
  <div class="cta"><span class="cta__label">Get In Today</span><span class="cta__phone"><svg viewBox="0 0 24 24" fill="none" stroke="#000" stroke-width="1.6"><circle cx="12" cy="12" r="10"/><path d="M9 7l2 3-1.5 1.5a7 7 0 0 0 3 3L14 13l3 2-1.5 2.5C11 17 7 13 6.5 8.5z" fill="#000"/></svg>0412-555-019</span></div>
</section>
</body>
</html>
```